Peanut Butter - Single Serve Sachet

We are a sports and wellness nutrition company (https://www.brightkelpfoods.in) and launching a new product Peanut Butter. Need attractive design of single serve sachet.

The product should be unique and eye catchy. It should have enough space to mention USPs later.

The product USP is tear-on the go sachet, image mockup has been attached.

Target Market(s)

Sports Persons and General Public looking for Peanut Butter.

Industry/Entity Type

Nutrition

Colors

Designer to choose colors to be used in the design.

Requirements
Must have
• Single serve sachet design. Attractive colour theme with Peanut Butter mentioned as bold.
Should not have
• no black colour

Files

```html
<!DOCTYPE html>
<html lang="en">
<head>
<meta charset="utf-8">
<title>Peanut Butter Sachet</title>
<link rel="stylesheet" href="https://fonts.googleapis.com/css2?family=Arimo:wght@400&display=swap">
<style>
  :root {
    --navy: #00152d;
    --orange: #ff650b;
    --cloud: #f1f2f1;
  }
  html, body {
    margin: 0;
    padding: 0;
    overflow: hidden;
    background: var(--cloud);
  }
  .sachet {
    display: block;
    width: 900px;
    height: 1200px;
    font-family: "Arimo", Arial, sans-serif;
  }
  .panel-top { fill: var(--navy); }
  .panel-bottom { fill: var(--orange); }
  .stripe { fill: var(--cloud); }
  .brand-slot { fill: var(--cloud); font-size: 58px; }
  .product-name { fill: var(--orange); font-size: 185px; }
  .rule { stroke: var(--orange); stroke-width: 2.5; }
  .category { fill: var(--cloud); font-size: 55px; }
  .category-dot { fill: none; stroke: var(--cloud); stroke-width: 2; }
  .description { fill: var(--navy); font-size: 35px; }
</style>
</head>
<body>
<svg class="sachet" viewBox="0 0 900 1200" xmlns="http://www.w3.org/2000/svg">
  <!-- panels -->
  <rect class="panel-top" x="0" y="0" width="900" height="818"/>
  <rect class="panel-bottom" x="0" y="818" width="900" height="382"/>

  <!-- top stripes -->
  <polygon class="stripe" points="0,119 612,0 748,0 0,144"/>
  <polygon class="stripe" points="0,171 900,5 900,0 870,0 900,0 900,50 0,216"/>
  <polygon class="stripe" points="755,0 900,0 900,5 0,171 0,160"/>

  <!-- brand slot -->
  <text class="brand-slot" x="13" y="263" textLength="840" lengthAdjust="spacing">PUT LOGO BRAND HERE</text>

  <!-- product name -->
  <text class="product-name" x="97" y="447" textLength="705" lengthAdjust="spacingAndGlyphs">PEANUT</text>
  <text class="product-name" x="104" y="627" textLength="693" lengthAdjust="spacingAndGlyphs">BUTTER</text>

  <!-- category band -->
  <line class="rule" x1="113" y1="707" x2="788" y2="707"/>
  <line class="rule" x1="113" y1="770" x2="788" y2="770"/>
  <rect class="category-dot" x="241" y="734" width="7" height="8"/>
  <text class="category" x="258" y="759" textLength="374" lengthAdjust="spacing">NUTRITION</text>
  <rect class="category-dot" x="643" y="734" width="7" height="8"/>

  <!-- description -->
  <text class="description" x="227" y="881" textLength="449" lengthAdjust="spacingAndGlyphs">DESCRIPTION OF PRODUCT</text>

  <!-- bottom stripes -->
  <polygon class="stripe" points="0,1147 900,975 900,1029 0,1200"/>
  <polygon class="stripe" points="132,1200 900,1054 900,1079 273,1200"/>
</svg>
</body>
</html>
```